Wool Product Label / Yarn Band

Looking to update the packaging on our wool products. This includes a design for a paper band to place around braided wool or yarn, and a design for a sticker to place on the outside of tissue paper wrapping. Open to updating or modifying the logo, which does not fit well on a round sticker, but the sticker could also be something wool related (like a sheep or drop spindle) that does not include the logo.
Target Market(s)
Wool crafters (knitters / spinners / felters). Mainly women, aged 30-70
Industry/Entity Type
Textile
Colors
Designer to choose colors to be used in the design.
Requirements
Must have
- Band needs to include, brand name, logo, url (fernloomery.net), dyelot number, as well as the fiber content (ex: Merino Wool) and weight of the fiber (ex: 4oz).
Nice to have
- Band would ideally be easily customized because the weight and fiber content is variable and will be printed specifically for each product, Variable information can be on a sticker or printed directly on a band that can be printed on a standard printer. Attached is a photo of the current band and it's application.

```html
<!DOCTYPE html>
<html lang="en">
<head>
<meta charset="utf-8">
<title>fernloomery yarn band</title>
<link rel="stylesheet" href="https://fonts.googleapis.com/css2?family=Lato:wght@400;700&family=Roboto+Condensed:wght@400;700&display=swap">
<style>
  :root {
    --ink: #3a3a3c;
    --frame: #4a4a4c;
    --brand-green: #6cb33f;
    --tag-grey: #58595b;
    --pill-red: #c9252b;
    --pill-orange: #e68a22;
    --warm: #f4c27e;
    --butter: #f2e79a;
    --lime: #d9e69a;
    --mint: #a9dcc8;
    --teal: #7cc4c0;
    --white: #ffffff;
  }
  * { margin: 0; padding: 0; box-sizing: border-box; }
  html, body { width: 1200px; height: 403px; overflow: hidden; background: #ffffff; }
  .yarn-band {
    position: relative;
    width: 1200px;
    height: 403px;
    overflow: hidden;
    font-family: "Lato", sans-serif;
  }
  .knit-field {
    position: absolute;
    inset: 0;
    background: linear-gradient(90deg, var(--warm) 0%, var(--butter) 30%, var(--lime) 55%, var(--mint) 80%, var(--teal) 100%);
  }
  .center-frame { position: absolute; inset: 0; width: 1200px; height: 403px; }
  .dyelot {
    position: absolute;
    left: 164px;
    top: 201px;
    transform: translate(-50%, -50%) rotate(90deg);
    white-space: nowrap;
    font-weight: 700;
    font-size: 22px;
    letter-spacing: 0.5px;
    color: var(--ink);
  }
  .site-url {
    position: absolute;
    left: 1038px;
    top: 201px;
    transform: translate(-50%, -50%) rotate(-90deg);
    white-space: nowrap;
    font-weight: 700;
    font-size: 22px;
    color: var(--ink);
  }
  .brand-name {
    position: absolute;
    left: 0; right: 0;
    top: 74px;
    text-align: center;
    font-family: "Roboto Condensed", sans-serif;
    font-weight: 700;
    font-size: 84px;
    line-height: 1;
    letter-spacing: -1px;
    color: var(--brand-green);
  }
  .tagline {
    position: absolute;
    left: 0; right: 0;
    top: 188px;
    text-align: center;
    font-family: "Roboto Condensed", sans-serif;
    font-weight: 700;
    font-size: 25px;
    color: var(--tag-grey);
  }
  .fiber-content {
    position: absolute;
    left: 408px;
    top: 247px;
    width: 384px;
    height: 62px;
    border-radius: 31px;
    background: linear-gradient(90deg, var(--pill-red) 0%, #d2322a 45%, var(--pill-orange) 100%);
    color: var(--white);
    font-weight: 700;
    font-size: 23px;
    display: flex;
    align-items: center;
    justify-content: center;
  }
  .weight {
    position: absolute;
    left: 0; right: 0;
    top: 322px;
    text-align: center;
    font-weight: 700;
    font-size: 24px;
    color: var(--tag-grey);
  }
</style>
</head>
<body>
  <main class="yarn-band">
    <div class="knit-field" role="img" aria-label="Pastel knit stitch pattern fading from peach and butter yellow to mint and teal"></div>

    <svg class="center-frame" viewBox="0 0 1200 403" aria-hidden="true">
      <defs>
        <linearGradient id="frameLine" x1="0" x2="1" y1="0" y2="0">
          <stop offset="0" stop-color="#d9a21b"/>
          <stop offset="0.5" stop-color="#6cb33f"/>
          <stop offset="1" stop-color="#1e6f86"/>
        </linearGradient>
      </defs>
      <path fill="var(--frame)" d="M330 50 L480 50 Q520 5 600 5 Q680 5 720 50 L870 50 Q905 50 910 85 Q950 95 950 201 Q950 307 910 318 Q905 353 870 353 L720 353 Q680 398 600 398 Q520 398 480 353 L330 353 Q295 353 290 318 Q250 307 250 201 Q250 95 290 85 Q295 50 330 50 Z"/>
      <g transform="translate(600 201) scale(0.972 0.93) translate(-600 -201)">
        <path fill="#ffffff" stroke="url(#frameLine)" stroke-width="4" d="M330 50 L480 50 Q520 5 600 5 Q680 5 720 50 L870 50 Q905 50 910 85 Q950 95 950 201 Q950 307 910 318 Q905 353 870 353 L720 353 Q680 398 600 398 Q520 398 480 353 L330 353 Q295 353 290 318 Q250 307 250 201 Q250 95 290 85 Q295 50 330 50 Z"/>
      </g>
      <g transform="translate(600 201) scale(0.94 0.86) translate(-600 -201)">
        <path fill="none" stroke="url(#frameLine)" stroke-width="1.2" d="M330 50 L480 50 Q520 5 600 5 Q680 5 720 50 L870 50 Q905 50 910 85 Q950 95 950 201 Q950 307 910 318 Q905 353 870 353 L720 353 Q680 398 600 398 Q520 398 480 353 L330 353 Q295 353 290 318 Q250 307 250 201 Q250 95 290 85 Q295 50 330 50 Z"/>
      </g>
    </svg>

    <p class="dyelot">S/N: MER/SILK-BLEND1</p>
    <h1 class="brand-name">fernloomery</h1>
    <p class="tagline">hand painted yarn &amp; fibers</p>
    <p class="fiber-content">85% Merino Wool | 15% Silk</p>
    <p class="weight">Qty: 4oz</p>
    <p class="site-url">www.fernloomery.net</p>
  </main>
</body>
</html>
```